Korrin Baptiste Law website for a law firm

modern clean website for a small boutique law firm. Based in Sacramento, CA and the Bay Area. Practice areas of Family Law, Civil litigation, and Criminal Defense. We already have a logo design as well as attorney pictures to include on page.
Would like images of California included on site.
Would like site to go with Logo that is already designed...blue/grey/white colors.

Industry/Entity Type

Law Firm

Number of Pages Required

5+ page

Requirements
Must have
• I already have several pages of content drafted. Just need the pages with images to input content. Must be clean and modern feel. Want it to reflect California and small boutique feel that is provided personalized legal attention.
• Must have a page where I can blog or post articles on.

```html
<!DOCTYPE html>
<html lang="en">
<head>
<meta charset="utf-8">
<title>Korrin &amp; Baptiste Law</title>
<link rel="stylesheet" href="https://fonts.googleapis.com/css2?family=Gelasio:wght@400;700&family=Montserrat:wght@400;500;600&display=swap">
<style>
:root{
  --blue:#3d8fe0;
  --blue-dark:#1f5fa8;
  --brand:#4f7fb5;
  --ink:#2b2b2b;
  --line:#d9dde3;
  --white:#ffffff;
  --footer:#2a2a2a;
  --serif:"Gelasio",Georgia,serif;
  --sans:"Montserrat",Arial,sans-serif;
}
*{box-sizing:border-box;margin:0;padding:0}
html,body{width:1200px;height:2528px;overflow:hidden;background:var(--white);font-family:var(--serif);color:var(--ink)}
.page{position:relative;width:1200px;height:2528px;overflow:hidden}
.abs{position:absolute}

/* header */
.site-header{position:absolute;left:0;top:0;width:1200px;height:110px;background:var(--white)}
.top-accent{position:absolute;left:0;top:0;width:606px;height:4px;background:var(--blue)}
.brand{position:absolute;left:86px;top:30px;font-family:var(--serif);font-weight:400;font-size:46px;color:var(--brand);line-height:1}
.main-nav{position:absolute;top:53px;left:0;width:1200px;font-size:15px;color:var(--ink)}
.main-nav span{position:absolute;white-space:nowrap}
.main-nav .active{color:var(--blue);border-left:1px solid var(--blue);border-right:1px solid var(--blue);padding:5px 12px;top:-6px}

/* hero */
.hero{position:absolute;left:0;top:110px;width:1200px;height:567px;
  background:
    radial-gradient(ellipse 260px 320px at 600px 330px,rgba(214,200,168,.85),rgba(214,200,168,0) 100%),
    radial-gradient(ellipse 230px 420px at 90px 380px,rgba(40,58,38,.9),rgba(40,58,38,0) 100%),
    radial-gradient(ellipse 230px 420px at 1110px 380px,rgba(40,58,38,.9),rgba(40,58,38,0) 100%),
    linear-gradient(180deg,#7f8fa3 0%,#a2aab2 35%,#8c8a78 70%,#4e5744 100%)}
.hero-shade{position:absolute;inset:0;background:rgba(30,40,55,.18)}
.hero-title{position:absolute;left:0;width:1200px;text-align:center;color:var(--white);text-shadow:0 2px 6px rgba(0,0,0,.45)}
.hero-kicker{top:234px;font-size:30px}
.hero-name{top:272px;font-size:46px;font-weight:700;letter-spacing:1px}
.hero-arrow{position:absolute;top:264px}

/* about */
.about{position:absolute;left:0;top:677px;width:1200px;height:385px;background:linear-gradient(90deg,#ecebe7 0%,#e0dad4 50%,#ecebe7 100%)}
.about-shape{position:absolute;left:0;top:0}
.section-title{position:absolute;left:0;width:1200px;text-align:center;font-weight:700;color:var(--ink)}
.divider{position:absolute;left:484px}
.about-text{position:absolute;left:88px;top:152px;width:1024px;text-align:center;font-size:13px;line-height:24px;color:#444}
.btn-outline{position:absolute;left:532px;top:258px;width:135px;height:42px;border:1px solid var(--blue);border-radius:21px;font-family:var(--sans);font-size:15px;color:var(--blue-dark);text-align:center;line-height:40px;background:rgba(255,255,255,.6)}

/* practice */
.practice-item{position:absolute;top:1234px;width:220px;text-align:center}
.practice-item svg{display:block;margin:0 auto}
.practice-label{margin-top:12px;font-size:17px;font-weight:700;color:var(--ink);white-space:nowrap}

/* team */
.team-band{position:absolute;left:0;top:1415px;width:1200px;height:237px;background:linear-gradient(180deg,#1f2f45 0%,#2c3d55 55%,#37506c 100%)}
.team-card{position:absolute;top:1565px;width:236px;height:295px;background:var(--white);box-shadow:0 6px 10px rgba(0,0,0,.12);text-align:center}
.avatar{position:absolute;left:62px;top:22px;width:112px;height:112px;border-radius:50%;border:4px solid var(--blue);padding:4px;background:var(--white)}
.avatar div{width:100%;height:100%;border-radius:50%;background:linear-gradient(160deg,#d7d1cb,#7b6d62)}
.member-name{position:absolute;top:151px;width:100%;font-size:17px}
.member-role{position:absolute;top:178px;width:100%;font-size:12px;color:var(--blue)}
.member-bio{position:absolute;top:205px;left:18px;width:200px;font-size:12px;line-height:19px;color:#666}

/* newsletter */
.newsletter{position:absolute;left:0;top:1929px;width:1200px;height:91px;border-top:1px solid var(--line)}
.newsletter-band{position:absolute;left:0;top:0}
.newsletter-title{position:absolute;left:86px;top:26px;font-family:var(--sans);font-weight:500;font-size:29px;color:var(--white);white-space:nowrap}
.news-input{position:absolute;left:554px;top:22px;width:420px;height:47px;border:1px solid #bbb;font-family:var(--sans);font-size:12px;color:#666;padding:15px 20px}
.news-btn{position:absolute;left:974px;top:22px;width:138px;height:47px;background:var(--blue);color:var(--white);font-family:var(--sans);font-size:19px;text-align:center;line-height:47px;border-radius:0 6px 6px 0}

/* contact */
.contact{position:absolute;left:0;top:2020px;width:1200px;height:457px;background:linear-gradient(90deg,#8a5a45 0%,#a87a5f 40%,#7a5040 100%)}
.touch-panel{position:absolute;left:88px;top:0;width:456px;height:457px;background:rgba(238,236,233,.93);text-align:center;font-family:var(--sans);font-size:14px;color:#333}
.touch-title{position:absolute;top:52px;width:100%;font-size:25px;font-weight:600;color:var(--blue-dark)}
.touch-item{position:absolute;width:100%;line-height:21px}
.touch-item svg{display:block;margin:0 auto 6px}
.form-panel{position:absolute;left:544px;top:0;width:568px;height:457px;background:rgba(30,80,150,.88);font-family:var(--sans);color:var(--white)}
.form-title{position:absolute;top:90px;width:100%;text-align:center;font-size:25px;font-weight:600}
.form-rule{position:absolute;left:262px;top:134px;width:44px;height:1px;background:var(--white)}
.field{position:absolute;left:39px;width:490px;height:46px;border:1px solid rgba(255,255,255,.7);font-size:12px;padding:13px 14px}
.field.comment{width:315px;height:89px}
.submit{position:absolute;left:395px;top:322px;width:134px;height:42px;background:var(--blue-dark);border-radius:4px;text-align:center;line-height:42px;font-size:19px;font-weight:600}

/* footer */
.site-footer{position:absolute;left:0;top:2477px;width:1200px;height:51px;background:var(--footer);font-family:var(--sans);font-size:11px;color:#bbb}
.site-footer .copy{position:absolute;left:88px;top:19px}
.social{position:absolute;top:19px;width:13px;height:13px;border-radius:50%;background:#cfcfcf}
</style>
</head>
<body>
<div class="page">

  <header class="site-header">
    <div class="top-accent"></div>
    <div class="brand">KBLAW</div>
    <nav class="main-nav">
      <span class="active" style="left:410px">Home</span>
      <span style="left:505px">About Us</span>
      <span style="left:612px">Elena R. Korrin</span>
      <span style="left:758px">Tomas J. Baptiste</span>
      <span style="left:920px">Practice Areas &#8964;</span>
      <span style="left:1060px">Contact</span>
    </nav>
  </header>

  <section class="hero" role="img" aria-label="California State Capitol dome in Sacramento framed by palm trees">
    <div class="hero-shade"></div>
    <div class="hero-title hero-kicker">Welcome to</div>
    <div class="hero-title hero-name">KORRIN &amp; BAPTISTE LAW</div>
    <svg class="hero-arrow" style="left:13px" width="58" height="38" viewBox="0 0 58 38"><path d="M0 19 L19 2 V13 H58 V25 H19 V36 Z" fill="#d8d8d8" opacity=".85"/></svg>
    <svg class="hero-arrow" style="left:1129px" width="58" height="38" viewBox="0 0 58 38"><path d="M58 19 L39 2 V13 H0 V25 H39 V36 Z" fill="#d8d8d8" opacity=".85"/></svg>
  </section>

  <section class="about">
    <div class="abs" style="left:0;top:0;width:1200px;height:385px" role="img" aria-label="Soft faded portrait of the two founding attorneys"></div>
    <svg class="about-shape" width="1200" height="385" viewBox="0 0 1200 385"><polygon points="0,266 600,385 0,385" fill="#fff"/><polygon points="1200,266 600,385 1200,385" fill="#fff"/></svg>
    <h2 class="section-title" style="top:56px;font-size:28px">About Korrin &amp; Baptiste Law</h2>
    <svg class="divider" style="top:100px" width="232" height="22" viewBox="0 0 232 22"><line x1="0" y1="11" x2="100" y2="11" stroke="#3d8fe0"/><line x1="132" y1="11" x2="232" y2="11" stroke="#3d8fe0"/><path d="M106 8 L116 2 L126 8 Z M107 9 H125 V10 H107 Z M109 11 H111 V17 H109 Z M115 11 H117 V17 H115 Z M121 11 H123 V17 H121 Z M106 18 H126 V20 H106 Z" fill="#3d8fe0"/></svg>
    <p class="about-text">Korrin &amp; Baptiste Law is a boutique business law firm representing small and midsize companies throughout Northern California. Our team of business law attorneys has substantial litigation and transactional experience. After earning his L.L.M. in Transnational Business Practices, our founding partner, Tomas Baptiste, dedicated his legal career to business transactions and civil litigation.</p>
    <div class="btn-outline">Learn More</div>
  </section>

  <section class="practice">
    <h2 class="section-title" style="top:1122px;font-size:28px">Our Practice Areas</h2>
    <svg class="divider" style="top:1170px" width="232" height="22" viewBox="0 0 232 22"><line x1="0" y1="11" x2="100" y2="11" stroke="#3d8fe0"/><line x1="132" y1="11" x2="232" y2="11" stroke="#3d8fe0"/><path d="M106 8 L116 2 L126 8 Z M107 9 H125 V10 H107 Z M109 11 H111 V17 H109 Z M115 11 H117 V17 H115 Z M121 11 H123 V17 H121 Z M106 18 H126 V20 H106 Z" fill="#3d8fe0"/></svg>
    <svg class="abs" style="left:70px;top:1266px" width="16" height="40" viewBox="0 0 16 40"><path d="M14 2 L2 20 L14 38" fill="none" stroke="#999" stroke-width="1.5"/></svg>
    <svg class="abs" style="left:1114px;top:1266px" width="16" height="40" viewBox="0 0 16 40"><path d="M2 2 L14 20 L2 38" fill="none" stroke="#999" stroke-width="1.5"/></svg>

    <div class="practice-item" style="left:67px">
      <svg width="92" height="92" viewBox="0 0 92 92"><circle cx="46" cy="46" r="44" fill="#fff" stroke="#8a8a8a" stroke-width="4"/><circle cx="46" cy="46" r="36" fill="#3d8fe0"/><rect x="30" y="52" width="6" height="10" fill="#fff"/><rect x="40" y="46" width="6" height="16" fill="#fff"/><rect x="50" y="40" width="6" height="22" fill="#fff"/><path d="M28 44 L42 34 L50 38 L62 28" fill="none" stroke="#fff" stroke-width="3"/></svg>
      <div class="practice-label">Business Law</div>
    </div>
    <div class="practice-item" style="left:278px">
      <svg width="92" height="92" viewBox="0 0 92 92"><circle cx="46" cy="46" r="44" fill="#fff" stroke="#8a8a8a" stroke-width="4"/><circle cx="46" cy="46" r="36" fill="#3d8fe0"/><rect x="33" y="26" width="26" height="36" fill="#fff"/><rect x="37" y="32" width="18" height="2" fill="#3d8fe0"/><rect x="37" y="38" width="18" height="2" fill="#3d8fe0"/><rect x="37" y="44" width="18" height="2" fill="#3d8fe0"/><rect x="37" y="52" width="10" height="5" fill="#3d8fe0"/></svg>
      <div class="practice-label">Business Formation</div>
    </div>
    <div class="practice-item" style="left:488px">
      <svg width="92" height="92" viewBox="0 0 92 92"><circle cx="46" cy="46" r="44" fill="#fff" stroke="#8a8a8a" stroke-width="4"/><circle cx="46" cy="46" r="36" fill="#3d8fe0"/><path d="M26 44 L36 36 L46 42 L56 36 L66 44 L52 56 L40 56 Z" fill="none" stroke="#fff" stroke-width="3" stroke-linejoin="round"/></svg>
      <div class="practice-label">Civil Litigation</div>
    </div>
    <div class="practice-item" style="left:699px">
      <svg width="92" height="92" viewBox="0 0 92 92"><circle cx="46" cy="46" r="44" fill="#fff" stroke="#8a8a8a" stroke-width="4"/><circle cx="46" cy="46" r="36" fill="#3d8fe0"/><path d="M28 46 L46 30 L64 46 M33 42 V62 H59 V42" fill="none" stroke="#fff" stroke-width="3"/><circle cx="43" cy="52" r="4" fill="none" stroke="#fff" stroke-width="2"/><circle cx="49" cy="52" r="4" fill="none" stroke="#fff" stroke-width="2"/></svg>
      <div class="practice-label">Family Law</div>
    </div>
    <div class="practice-item" style="left:909px">
      <svg width="92" height="92" viewBox="0 0 92 92"><circle cx="46" cy="46" r="44" fill="#fff" stroke="#8a8a8a" stroke-width="4"/><circle cx="46" cy="46" r="36" fill="#3d8fe0"/><path d="M32 48 V44 A14 14 0 0 1 60 44 V48" fill="none" stroke="#fff" stroke-width="3"/><rect x="29" y="46" width="7" height="11" rx="2" fill="#fff"/><rect x="56" y="46" width="7" height="11" rx="2" fill="#fff"/><path d="M59 57 Q58 63 48 63" fill="none" stroke="#fff" stroke-width="2"/></svg>
      <div class="practice-label">Spousal support</div>
    </div>
  </section>

  <section class="team">
    <div class="team-band" role="img" aria-label="Snow-capped Mount Shasta at dusk"></div>
    <h2 class="section-title" style="top:1452px;font-size:28px;color:#fff">Meet Our Team</h2>
    <svg class="divider" style="top:1497px" width="232" height="22" viewBox="0 0 232 22"><line x1="0" y1="11" x2="100" y2="11" stroke="#3d8fe0"/><line x1="132" y1="11" x2="232" y2="11" stroke="#3d8fe0"/><path d="M106 8 L116 2 L126 8 Z M107 9 H125 V10 H107 Z M109 11 H111 V17 H109 Z M115 11 H117 V17 H115 Z M121 11 H123 V17 H121 Z M106 18 H126 V20 H106 Z" fill="#3d8fe0"/></svg>

    <article class="team-card" style="left:88px">
      <div class="avatar"><div role="img" aria-label="Portrait of attorney Elena R. Korrin"></div></div>
      <div class="member-name">Elena R. Korrin</div>
      <div class="member-role">Senior Partner</div>
      <p class="member-bio">Lorem ipsum dolor sit amet, con-<br>sectetur adipiscing elit. Curabitur<br>auctor mauris metus</p>
    </article>
    <article class="team-card" style="left:350px">
      <div class="avatar"><div role="img" aria-label="Portrait of attorney Tomas J. Baptiste"></div></div>
      <div class="member-name">Elena R. Korrin</div>
      <div class="member-role">Senior Partner</div>
      <p class="member-bio">Lorem ipsum dolor sit amet, con-<br>sectetur adipiscing elit. Curabitur<br>auctor mauris metus</p>
    </article>
    <article class="team-card" style="left:615px">
      <div class="avatar"><div role="img" aria-label="Portrait of a team attorney"></div></div>
      <div class="member-name">Elena R. Korrin</div>
      <div class="member-role">Senior Partner</div>
      <p class="member-bio">Lorem ipsum dolor sit amet, con-<br>sectetur adipiscing elit. Curabitur<br>auctor mauris metus</p>
    </article>
    <article class="team-card" style="left:878px">
      <div class="avatar"><div role="img" aria-label="Portrait of a team attorney"></div></div>
      <div class="member-name">Elena R. Korrin</div>
      <div class="member-role">Senior Partner</div>
      <p class="member-bio">Lorem ipsum dolor sit amet, con-<br>sectetur adipiscing elit. Curabitur<br>auctor mauris metus</p>
    </article>
  </section>

  <section class="newsletter">
    <svg class="newsletter-band" width="522" height="91" viewBox="0 0 522 91"><polygon points="0,0 522,0 496,91 0,91" fill="#4a9be6"/></svg>
    <div class="newsletter-title">Subscribe Our Newsletter</div>
    <div class="news-input">Enter your email</div>
    <div class="news-btn">Subscribe</div>
  </section>

  <section class="contact" role="img" aria-label="Attorney standing beside a red brick wall">
    <div class="touch-panel">
      <div class="touch-title">Get in touch</div>
      <div class="touch-item" style="top:118px">
        <svg width="22" height="20" viewBox="0 0 22 20"><path d="M1 4 L7 1 L15 4 L21 1 V16 L15 19 L7 16 L1 19 Z" fill="#3d8fe0"/></svg>
        418 Capitol Row, Suite 200<br>Sacramento, CA 95814
      </div>
      <div class="touch-item" style="top:210px">
        <svg width="18" height="18" viewBox="0 0 18 18"><path d="M4 1 L7 5 L5 7 Q7 11 11 13 L13 11 L17 14 L15 17 Q6 16 1 3 Z" fill="#3d8fe0"/></svg>
        Phone Number: (555) 014-2270
      </div>
      <div class="touch-item" style="top:282px">
        <svg width="22" height="20" viewBox="0 0 22 20"><path d="M1 8 L11 1 L21 8 V19 H1 Z" fill="#3d8fe0"/><path d="M1 8 L11 14 L21 8" fill="none" stroke="#fff" stroke-width="1.5"/></svg>
        Email: info@kbaptistelaw.com
      </div>
      <div class="touch-item" style="top:354px">
        <svg width="20" height="20" viewBox="0 0 20 20"><rect x="4" y="1" width="12" height="6" fill="#3d8fe0"/><rect x="1" y="7" width="18" height="12" rx="2" fill="#3d8fe0"/><rect x="5" y="11" width="10" height="2" fill="#fff"/></svg>
        Fax: (555) 014-2271
      </div>
    </div>
    <div class="form-panel">
      <div class="form-title">Contact Us</div>
      <div class="form-rule"></div>
      <div class="field" style="top:158px">Your Name</div>
      <div class="field" style="top:218px">Your Email</div>
      <div class="field comment" style="top:275px">Your Comment</div>
      <div class="submit">Submit</div>
    </div>
  </section>

  <footer class="site-footer">
    <span class="copy">Copyright 2017 Your Company Name Here</span>
    <span class="social" style="left:1028px"></span>
    <span class="social" style="left:1060px"></span>
    <span class="social" style="left:1099px"></span>
  </footer>

</div>
</body>
</html>
```